Master / Title Page for Event Planner Proposal

We design our proposals in Publisher. Attached is our current title page and inside pages. We are looking to update our template to something that is classy yet fun. We plan corporate picnics and holiday parties. Please see attached sample of past proposals. The inside pages need to have a design that is very flexible with the number of images used on the page. The image(s) on the cover page would not change. The cover page can have have many images or just one - whichever is best.

```html
<!DOCTYPE html>
<html lang="en">
<head>
<meta charset="utf-8">
<title>DJ, Bingo and Prizes</title>
<link rel="stylesheet" href="https://fonts.googleapis.com/css2?family=Poppins:ital,wght@0,400;0,600;0,700;1,600&display=swap">
<style>
  :root {
    --navy: #1f1f5e;
    --indigo: #3e3a93;
    --orange: #f06325;
    --sky: #8fb2e0;
    --red: #a51d1d;
    --ink: #111111;
    --rule: #8c8fb5;
    --paper: #ffffff;
    --mist: #e4f0fa;
  }
  * { margin: 0; padding: 0; box-sizing: border-box; }
  html, body { width: 848px; height: 1200px; overflow: hidden; background: var(--paper); }
  .page {
    position: relative;
    width: 848px;
    height: 1200px;
    overflow: hidden;
    font-family: "Poppins", sans-serif;
    background:
      radial-gradient(circle at 15% 75%, var(--mist) 0%, rgba(228,240,250,0) 45%),
      radial-gradient(circle at 85% 70%, var(--mist) 0%, rgba(228,240,250,0) 40%),
      linear-gradient(180deg, var(--paper) 45%, #eef5fc 70%, #f4f8fd 100%);
  }
  .header-wave { position: absolute; top: 0; left: 0; width: 848px; height: 300px; }
  .page-title {
    position: absolute; top: 44px; left: 0; width: 100%;
    text-align: center; color: var(--paper);
    font-weight: 700; font-size: 34px; letter-spacing: 0.2px;
  }
  .photo {
    position: absolute;
    border: 2px solid var(--orange);
    border-radius: 14px;
    overflow: hidden;
  }
  .photo-dj { left: 70px; top: 305px; width: 276px; height: 187px; background: linear-gradient(160deg, #b9c8d6, #3a3a3a 60%, #8a5a4a); }
  .photo-table { left: 362px; top: 305px; width: 124px; height: 187px; background: linear-gradient(170deg, #6b5648, #c9b9a8 55%, #5a4638); }
  .photo-card { left: 502px; top: 305px; width: 276px; height: 187px; background: linear-gradient(120deg, #6a6a6e, #d9b56a 45%, #d7d9dc 80%); }
  .photo-crowd { left: 68px; top: 845px; width: 339px; height: 263px; background: linear-gradient(150deg, #b4a58c, #6e7a5a 50%, #4d4c52); }
  .photo-prizes { left: 438px; top: 845px; width: 340px; height: 263px; background: linear-gradient(170deg, #9fb0a8, #7f9a52 45%, #5fa7d8 75%, #8fc25f); }
  .offer { position: absolute; top: 540px; left: 0; width: 100%; text-align: center; }
  .offer-heading { color: var(--indigo); font-weight: 700; font-size: 22px; line-height: 1.2; margin-bottom: 6px; }
  .offer-text { color: var(--indigo); font-size: 16px; line-height: 29px; }
  .offer-text + .offer-text { margin-top: 29px; }
  .offer-tagline { color: var(--red); font-style: italic; font-weight: 600; font-size: 17px; margin-top: 27px; }
  .offer-price { color: var(--ink); font-weight: 600; font-size: 16px; margin-top: 20px; }
  .footer { position: absolute; top: 1152px; left: 69px; width: 709px; display: flex; align-items: center; gap: 12px; }
  .footer-rule { flex: 1; height: 1px; background: var(--rule); }
  .footer-site { color: var(--indigo); font-size: 13px; letter-spacing: 0.2px; }
</style>
</head>
<body>
<main class="page">
  <svg class="header-wave" viewBox="0 0 848 300" aria-hidden="true">
    <defs>
      <linearGradient id="swoosh-orange" x1="0" y1="0" x2="1" y2="0">
        <stop offset="0" stop-color="#f06325"/>
        <stop offset="0.25" stop-color="#2a2460"/>
        <stop offset="0.6" stop-color="#a7484a"/>
        <stop offset="1" stop-color="#f26522"/>
      </linearGradient>
      <linearGradient id="swoosh-blue" x1="0" y1="0" x2="1" y2="0">
        <stop offset="0" stop-color="#1f2f6e"/>
        <stop offset="0.6" stop-color="#9bb8e6"/>
        <stop offset="1" stop-color="#3a5fae"/>
      </linearGradient>
    </defs>
    <path d="M0 0 H848 V230 C700 175 400 170 0 262 Z" fill="#1f1f5e"/>
    <path d="M0 102 C140 140 300 158 470 156 C630 152 760 108 848 118 V230 C760 190 640 170 450 168 C280 166 140 160 0 145 Z" fill="url(#swoosh-orange)"/>
    <path d="M0 86 C150 138 300 156 470 150 C640 144 760 96 848 108 V120 C760 108 640 150 470 160 C300 166 150 150 0 104 Z" fill="#ffffff"/>
    <path d="M450 170 C620 160 760 190 848 240 V290 C780 230 640 180 450 170 Z" fill="url(#swoosh-blue)"/>
    <path d="M848 290 C790 232 650 184 450 170 C640 178 790 205 848 246 Z" fill="#ffffff" opacity="0.35"/>
  </svg>

  <h1 class="page-title">DJ, BINGO AND PRIZES</h1>

  <div class="photo photo-dj" role="img" aria-label="Two DJs hosting a bingo game on a beach stage"></div>
  <div class="photo photo-table" role="img" aria-label="Guests at a long table marking bingo cards"></div>
  <div class="photo photo-card" role="img" aria-label="Guest holding a bingo card"></div>

  <section class="offer">
    <h2 class="offer-heading">DJ, BINGO AND PRIZES</h2>
    <p class="offer-text">Your event will be staffed with a professional DJ who will host<br>fun games of BINGO, dance contests and family friendly music throughout your event.</p>
    <p class="offer-text">Large and small quality prizes will be awarded approximately every 20 minutes.<br>Prizes may include: Burger Barn, Vine Table gift cards, Blenders, Toys</p>
    <p class="offer-tagline">You can expect high energy and lots of fun!</p>
    <p class="offer-price">$12,295.00</p>
  </section>

  <div class="photo photo-crowd" role="img" aria-label="Smiling guests at a patio table playing bingo with daubers"></div>
  <div class="photo photo-prizes" role="img" aria-label="Children browsing a prize table with toys and a blender on a lawn"></div>

  <footer class="footer">
    <span class="footer-rule"></span>
    <span class="footer-site">WWW.PARTYHARBOREVENTS.COM</span>
    <span class="footer-rule"></span>
  </footer>
</main>
</body>
</html>
```